Looking for a cool & simple business-card-design for digital agency

Hi!

We are a web agency that offers Reputation Management, Vextra & Seo Services and software development. We like cool things, we like innovative styles.

We have uploaded our logo.

Project Deadline Extended Reason: Client does not want any designs with the colorful logo. Please send us submissions ONLY with the blac and white logo. What the client would like to see:1) Back of the card: is a silver logo on a black background2) front of the card with all the data, please use white background and black logo thank you Added Friday, May 8, 2015

```html
<!DOCTYPE html>
<html lang="de">
<head>
<meta charset="utf-8">
<title>Pixelwerk – Geschäftsausstattung</title>
<link href="https://fonts.googleapis.com/css2?family=Open+Sans:wght@400;600;700;800&display=swap" rel="stylesheet">
<style>
  :root {
    --stage: #e4e4e4;
    --paper: #ffffff;
    --ink: #111111;
    --ink-soft: #333333;
    --steel: #5f5c5c;
    --silver: #cfcfcf;
    --shadow: rgba(0,0,0,0.28);
  }
  * { box-sizing: border-box; margin: 0; padding: 0; }
  html, body { width: 1200px; height: 934px; overflow: hidden; }
  body {
    background: var(--stage);
    font-family: "Open Sans", Arial, sans-serif;
    color: var(--ink);
    position: relative;
  }
  .sheet {
    position: absolute;
    background: var(--paper);
    box-shadow: 3px 5px 8px var(--shadow);
    overflow: hidden;
  }
  .sheet svg.swoosh { position: absolute; left: 0; top: 0; }
  .wordmark {
    position: absolute;
    font-weight: 800;
    letter-spacing: 0.2px;
    color: var(--ink);
    display: flex;
    align-items: center;
    gap: 7px;
    line-height: 1;
  }
  .wordmark .dot { width: 9px; height: 9px; background: currentColor; }

  /* Letterhead */
  .letterhead { left: 69px; top: 83px; width: 469px; height: 664px; }
  .letterhead .wordmark { left: 40px; top: 42px; font-size: 22px; }
  .letterhead .sender {
    position: absolute; right: 26px; top: 585px;
    text-align: right; font-size: 7px; line-height: 12px; color: var(--ink-soft);
  }
  .letterhead .sender .company { font-weight: 700; color: var(--ink); margin-bottom: 3px; }
  .letterhead .sender .item::after { content: " ●"; font-size: 5px; color: #777; }

  /* Envelope front */
  .envelope-front { left: 565px; top: 83px; width: 566px; height: 256px; }
  .envelope-front .wordmark { left: 28px; top: 36px; font-size: 22px; }
  .envelope-front .sender {
    position: absolute; left: 28px; top: 191px;
    font-size: 6.5px; line-height: 9px; color: var(--ink-soft);
  }
  .envelope-front .sender .address { margin-bottom: 8px; }
  .envelope-front .sender .item::before { content: "● "; font-size: 5px; color: #777; }

  /* Envelope back */
  .envelope-back { left: 565px; top: 366px; width: 566px; height: 255px; }
  .envelope-back .flap-url {
    position: absolute; left: 0; right: 0; top: 39px; text-align: center;
    font-size: 9px; letter-spacing: 2px; color: var(--silver);
  }
  .envelope-back .bottom-rule {
    position: absolute; left: 0; right: 0; bottom: 0; height: 7px; background: var(--ink);
  }

  /* Business cards */
  .card-back {
    left: 565px; top: 647px; width: 122px; height: 203px;
    background: linear-gradient(180deg, #3a3a3a 0%, #161616 55%, #0c0c0c 100%);
  }
  .card-back .wordmark {
    left: 0; right: 0; top: 108px; justify-content: center;
    font-size: 15px; color: var(--silver);
  }
  .card-back .wordmark .dot { width: 7px; height: 7px; }
  .card-back .base { position: absolute; left: 0; right: 0; bottom: 0; height: 8px; background: #8a8a8a; }

  .card-front {
    left: 726px; top: 647px; width: 122px; height: 203px;
    border-left: 5px solid var(--ink);
  }
  .card-front .wordmark { left: 0; right: 0; top: 82px; justify-content: center; font-size: 14px; }
  .card-front .wordmark .dot { width: 7px; height: 7px; }
  .card-front .person { position: absolute; left: 11px; top: 131px; }
  .card-front .person .name { font-size: 7.5px; font-weight: 600; }
  .card-front .person .role { font-size: 4.5px; color: var(--ink-soft); margin-top: 1px; }
  .card-front .contact {
    position: absolute; left: 11px; top: 164px;
    font-size: 4.3px; line-height: 6.4px; color: var(--ink-soft);
  }
  .card-front .contact .item::before { content: "● "; font-size: 3.5px; }
</style>
</head>
<body>

  <section class="sheet letterhead" aria-label="Briefbogen">
    <svg class="swoosh" width="469" height="664" viewBox="0 0 469 664" aria-hidden="true">
      <defs>
        <linearGradient id="lh-black" x1="0" y1="0" x2="1" y2="0">
          <stop offset="0" stop-color="#111"/><stop offset="0.6" stop-color="#3a3a3a"/><stop offset="1" stop-color="#111"/>
        </linearGradient>
      </defs>
      <path d="M10,0 Q260,6 469,34 L469,0 Z" fill="url(#lh-black)"/>
      <path d="M120,0 Q320,14 469,58 L469,44 Q320,8 180,0 Z" fill="var(--steel)"/>
      <path d="M0,570 Q180,598 330,636 Q170,606 0,586 Z" fill="var(--steel)"/>
      <path d="M0,595 Q230,630 469,664 L0,664 Z" fill="url(#lh-black)"/>
    </svg>
    <div class="wordmark"><span class="dot"></span>Pixelwerk</div>
    <div class="sender">
      <div class="company">Pixelwerk LLC</div>
      <div>Your Commercial or office address</div>
      <div class="item">00.00.00.0000</div>
      <div class="item">yourname@yourwebsite.com</div>
      <div class="item">www.yourwebsite.com</div>
    </div>
  </section>

  <section class="sheet envelope-front" aria-label="Umschlag Vorderseite">
    <svg class="swoosh" width="566" height="256" viewBox="0 0 566 256" aria-hidden="true">
      <path d="M160,236 Q370,204 566,182 L566,196 Q370,218 160,236 Z" fill="var(--steel)"/>
      <path d="M0,256 Q300,222 566,204 L566,256 Z" fill="var(--ink)"/>
    </svg>
    <div class="wordmark"><span class="dot"></span>Pixelwerk</div>
    <div class="sender">
      <div class="address">Your Commercial or office address</div>
      <div class="item">00.00.00.0000</div>
      <div class="item">yourname@yourwebsite.com</div>
      <div class="item">www.yourwebsite.com</div>
    </div>
  </section>

  <section class="sheet envelope-back" aria-label="Umschlag Rückseite">
    <svg class="swoosh" width="566" height="255" viewBox="0 0 566 255" aria-hidden="true">
      <path d="M0,0 L566,0 L566,4 L530,90 L36,90 L0,4 Z" fill="var(--ink)"/>
    </svg>
    <div class="flap-url">www.pixelwerk.com</div>
    <div class="bottom-rule"></div>
  </section>

  <section class="sheet card-back" aria-label="Visitenkarte Rückseite">
    <div class="wordmark"><span class="dot"></span>Pixelwerk</div>
    <div class="base"></div>
  </section>

  <section class="sheet card-front" aria-label="Visitenkarte Vorderseite">
    <div class="wordmark"><span class="dot"></span>Pixelwerk</div>
    <div class="person">
      <div class="name">Your Long Name</div>
      <div class="role">Managing Director</div>
    </div>
    <div class="contact">
      <div class="item">Your office address here</div>
      <div class="item">00.00.00.000 · 00.00.00.000</div>
      <div class="item">yourname@yourwebsite.com</div>
      <div class="item">www.yourwebsite.com</div>
    </div>
  </section>

</body>
</html>
```